Harlowe Skid Service Business Cards

WHAT WE DOWe RepairWe CustomizeWe ManufactureWe Deliver
Reason: Hello,
I would like to extend the deadline to May 1st - no additional fee. Reason being is because I am waiting on a reply from feedback from the designed that we are planning on choosing. I would like an answer as soon as possible, please and thanks!!!
Industry/Entity Type
Business
Contact Information for Business Card
Mireya Quintanal
Vice President
Office: 847-555-0142
Cell: 708-555-0187
Fax: 847-555-0163
mireya@harloweskid.com
Harlowe Skid Service II, Inc
2290 Fernhollow Avenue
Ashdale Village, IL 60999
www.harloweskid.com
Look and feel
Each slider illustrates characteristics of the customer's brand and the style your logo design should communicate.

```html
<!DOCTYPE html>
<html lang="en">
<head>
<meta charset="utf-8">
<title>Harlowe Skid Service – Business Card</title>
<link rel="stylesheet" href="https://fonts.googleapis.com/css2?family=Open+Sans:wght@400;600;700&display=swap">
<style>
  :root {
    --stage: #e9e6e2;
    --card: #ffffff;
    --brand-blue: #0a6ff5;
    --ink: #111111;
    --on-blue: #ffffff;
  }
  * { margin: 0; padding: 0; box-sizing: border-box; }
  html, body {
    width: 1200px; height: 900px; overflow: hidden;
    background: var(--stage);
    font-family: "Open Sans", Arial, sans-serif;
  }
  .business-card {
    position: absolute; left: 100px; top: 140px;
    width: 1000px; height: 620px;
    background: var(--card);
    box-shadow: 0 10px 30px rgba(0,0,0,0.18);
    overflow: hidden;
  }
  .wave-band { position: absolute; inset: 0; width: 100%; height: 100%; }
  .holder { position: absolute; right: 51px; top: 58px; text-align: right; }
  .holder-name { color: var(--brand-blue); font-weight: 600; font-size: 36px; line-height: 1.15; }
  .holder-title { color: var(--ink); font-size: 25px; line-height: 1.2; }
  .company-mark {
    position: absolute; left: 62px; top: 170px;
    display: flex; align-items: center; gap: 22px;
  }
  .mark-square { width: 70px; height: 70px; background: var(--brand-blue); flex: none; }
  .mark-name {
    color: var(--ink); font-weight: 700; font-size: 50px; line-height: 1.05;
    text-transform: uppercase; letter-spacing: 0.5px;
  }
  .contact-list {
    position: absolute; right: 48px; top: 352px;
    list-style: none; text-align: right;
    color: var(--on-blue); font-size: 25px; line-height: 41px;
  }
  .contact-list li { display: flex; justify-content: flex-end; align-items: center; gap: 10px; }
  .contact-list svg { width: 20px; height: 20px; fill: var(--on-blue); }
  .company-legal {
    position: absolute; right: 51px; top: 490px;
    color: var(--on-blue); font-weight: 600; font-size: 27px;
  }
  .company-address {
    position: absolute; right: 51px; top: 545px;
    color: var(--on-blue); font-size: 24px; white-space: nowrap;
  }
</style>
</head>
<body>
  <section class="business-card">
    <svg class="wave-band" viewBox="0 0 652 404" preserveAspectRatio="none" aria-hidden="true">
      <path d="M0,254 C80,305 150,344 222,336 C330,324 420,176 560,178 C610,180 640,200 652,220 L652,404 L0,404 Z" fill="var(--brand-blue)"/>
      <path d="M0,242 C80,294 150,332 222,324 C330,312 420,162 560,164 C610,166 640,186 652,206" fill="none" stroke="var(--ink)" stroke-width="6"/>
    </svg>

    <header class="holder">
      <p class="holder-name">Mireya Quintanal</p>
      <p class="holder-title">Vice President</p>
    </header>

    <div class="company-mark">
      <span class="mark-square"></span>
      <p class="mark-name">Harlowe Skid<br>Service</p>
    </div>

    <ul class="contact-list">
      <li>847-555-0142
        <svg viewBox="0 0 24 24"><path d="M6.6 10.8a15 15 0 0 0 6.6 6.6l2.2-2.2a1 1 0 0 1 1-.25 11.4 11.4 0 0 0 3.6.57 1 1 0 0 1 1 1V20a1 1 0 0 1-1 1A17 17 0 0 1 3 4a1 1 0 0 1 1-1h3.5a1 1 0 0 1 1 1c0 1.25.2 2.45.57 3.57a1 1 0 0 1-.25 1z"/></svg>
      </li>
      <li>708-555-0187
        <svg viewBox="0 0 24 24"><path d="M7 1h10a2 2 0 0 1 2 2v18a2 2 0 0 1-2 2H7a2 2 0 0 1-2-2V3a2 2 0 0 1 2-2zm0 3v14h10V4zm5 15.5a1 1 0 1 0 0 2 1 1 0 0 0 0-2z"/></svg>
      </li>
      <li>847-555-0163
        <svg viewBox="0 0 24 24"><path d="M6 2h9l3 3v4h1a3 3 0 0 1 3 3v9H2v-9a3 3 0 0 1 3-3h1zm2 2v5h8V6h-2V4zm-3 8v7h14v-7zm2 2h4v2H7z"/></svg>
      </li>
    </ul>

    <p class="company-legal">Harlowe Skid Service II, Inc</p>
    <p class="company-address">2290 Fernhollow Avenue Ashdale Village, IL 60999</p>
  </section>
</body>
</html>
```